Bin Sentinel sales and convention information

The product is called the Bin Sentinel. It's a commercial grade product designed to prevent dumpster drivers from damaging the enclosures the dumpsters are stored in by "Holding the Line" from the drivers. They also prevent the dumpsters from being misplaced on the property as well as being moved by vandals during acts of arson. Visit www.the bin sentinel.example for a complete understanding of the product. Specifically visit the home page and the story section of the site.

Target Market(s)

Commercial property owners, Commercial property managers, Reits, sanitation companies, architects, designers, engineers, township building departments, fire marshals, code enforcement departments.

Industry/Entity Type

Commercial

Colors
fbed22
ec1f27
000000
959595

Requirements
Must have
• Must have the black and gold logo provided. The Standard Bin Sentinel shown as the dominant seller. Brochure should flow rather then being boxy. The use of color.
• We would like to see the before and after pics. and description feature prominent on the an inside page. This is our selling point.
Nice to have
• We were not happy with the pics. and would like to see the labels removed from the dumpsters. They are a distraction.
• The Standard- Bin Sentinel is our primary seller and should be the dominant pic.
Should not have
• Do not include my phone number, should not include the address other then the P.O. Box. Should not include the complete installation instructions.

```html
<!DOCTYPE html>
<html lang="en">
<head>
<meta charset="utf-8">
<title>Bin Sentinel – Brochure Inside Spread</title>
<link href="https://fonts.googleapis.com/css2?family=Arimo:ital,wght@0,400;0,700;1,400;1,700&family=Roboto:wght@300&display=swap" rel="stylesheet">
<style>
  :root{
    --gold:#fbed22;
    --red:#ec1f27;
    --black:#000000;
    --grey:#959595;
    --ink:#1d1d1d;
    --navy:#1f3a7a;
    --paper:#ffffff;
  }
  *{box-sizing:border-box;margin:0;padding:0}
  html,body{width:1200px;height:927px;overflow:hidden;background:var(--paper)}
  body{font-family:"Arimo",Arial,sans-serif;color:var(--ink);position:relative}
  .backdrop{position:absolute;left:0;top:360px;width:1200px;height:567px;
    background:linear-gradient(180deg,#ffffff 0%,#eef0f1 25%,#e3e6e8 70%,#ebebe6 100%)}
  .section-bracket{position:absolute}
  .section-bracket svg{display:block;overflow:visible}
  .section-bracket .label{position:absolute;top:3px;left:0;right:0;text-align:center;
    font-weight:700;font-size:14.5px;letter-spacing:.2px;color:var(--black)}
  .photo{position:absolute}
  .text{position:absolute;font-size:13px;line-height:16.4px}
  .text p{margin-bottom:16.4px}
  .brand{color:var(--red);font-style:italic}
  .strong{font-weight:700;color:var(--black)}
  .quote{position:absolute;left:43px;top:742px;font-family:"Roboto",Arial,sans-serif;
    font-weight:300;font-size:41px;line-height:37px;color:var(--navy);letter-spacing:-.5px}
  .usa{position:absolute;left:440px;top:793px;width:320px;text-align:center;font-size:13.5px}
  .usa svg{display:block;margin:0 auto 12px}
  .usa .made{font-weight:700;font-size:18px;color:var(--black);margin-top:3px}
</style>
</head>
<body>

<div class="backdrop" role="img" aria-label="Faint background photo of dumpsters in an enclosure"></div>

<!-- Before & After header -->
<div class="section-bracket" style="left:40px;top:42px;width:742px">
  <svg width="742" height="56">
    <path d="M11,56 V24 Q11,14 24,14 H700 Q734,14 734,50 V56" fill="none" stroke="#d0d0d0" stroke-width="16" transform="translate(4,4)"/>
    <path d="M11,56 V24 Q11,14 24,14 H700 Q734,14 734,50 V56" fill="none" stroke="var(--gold)" stroke-width="16"/>
  </svg>
  <div class="label">BEFORE &amp; AFTER</div>
</div>

<div class="photo" style="left:43px;top:118px;width:360px;height:240px;background:linear-gradient(160deg,#c9c2b2,#9c9485 60%,#6e675c)" role="img" aria-label="Before: damaged block dumpster enclosure with debris"></div>
<div class="photo" style="left:403px;top:118px;width:360px;height:240px;background:linear-gradient(180deg,#b9c7d8 0%,#d9cfb9 30%,#2f5a45 55%,#2a4e3c 80%,#c8c4b8 100%)" role="img" aria-label="After: green dumpster held by yellow guard rails inside a clean enclosure"></div>

<div class="text" style="left:43px;top:392px;width:330px">
  <p>As a commercial real estate owners, we constantly strive to maintain the look and integrity of our properties.</p>
  <p>The dumpster enclosure is the most overlooked area of a commercial property site and the most likely to be damaged by the carelessness of others. Whenever we develop a new property, little attention was placed on protecting the walls of the dumpster enclosure as well as the control of the placement of the dumpster container dump site. We have used the standard practice of installing bollards within the enclosures, but not surprisingly, the enclosure walls were still being damaged. Needless and costly repairs sparked an idea as simple as the hula hoop.</p>
  <p><span class="brand">The Bin Sentinel™.</span> If we could control the removal and replacement of the dumpster, our problem would be solved.</p>
</div>

<div class="text" style="left:436px;top:392px;width:330px">
  <p class="strong">The average cost of repairing or replacing a damaged dumpster enclosure is between $1500 - $7000 with no guarantees that the same damage will not occur again.</p>
  <p><span class="brand">The Bin Sentinel™</span> provides the added assurance by preventing the problem.</p>
  <p><span class="brand">The Bin Sentinel™</span> was developed for the purpose of <span class="brand" style="font-weight:700">"Holding the Line"</span>. Engineered and patented, our product has been installed and tested at many of our franchise locations such as Brewline Coffee, Pancake Porch, Ringside Donuts and Festival Depot.</p>
  <p>These locations were chosen because of their excessive turnover of dumpster containers and were associated with their enclosures. The Bin Sentinel™ has exceeded our expectations.</p>
</div>

<div class="quote">"The best ideas<br>comes from<br>solving problems".</div>

<div class="usa">
  <svg width="134" height="48" viewBox="0 0 134 48" aria-label="American flag">
    <g>
      <rect width="134" height="48" fill="#fff"/>
      <rect y="0" width="134" height="3.7" fill="#c8102e"/>
      <rect y="7.4" width="134" height="3.7" fill="#c8102e"/>
      <rect y="14.8" width="134" height="3.7" fill="#c8102e"/>
      <rect y="22.2" width="134" height="3.7" fill="#c8102e"/>
      <rect y="29.6" width="134" height="3.7" fill="#c8102e"/>
      <rect y="37" width="134" height="3.7" fill="#c8102e"/>
      <rect y="44.3" width="134" height="3.7" fill="#c8102e"/>
      <rect width="56" height="26" fill="#1f3a7a"/>
    </g>
  </svg>
  We are proud to offer a product that is
  <div class="made">"Made in the USA".</div>
</div>

<!-- Standard -->
<div class="section-bracket" style="left:828px;top:42px;width:342px">
  <svg width="342" height="56">
    <path d="M11,56 V24 Q11,14 24,14 H300 Q334,14 334,50 V56" fill="none" stroke="#d0d0d0" stroke-width="16" transform="translate(4,4)"/>
    <path d="M11,56 V24 Q11,14 24,14 H300 Q334,14 334,50 V56" fill="none" stroke="var(--gold)" stroke-width="16"/>
  </svg>
  <div class="label">STANDARD</div>
</div>

<div class="photo" style="left:836px;top:110px;width:168px;height:150px;background:radial-gradient(ellipse at 50% 45%,#2e5244 0%,#24463a 45%,#ffffff 72%)" role="img" aria-label="Green dumpster with the yellow Standard Bin Sentinel rail"></div>
<div class="text" style="left:1006px;top:132px;width:170px">
  <span class="brand">The Bin Sentinel™</span><br>is designed to provide maximum protection of masonry enclosures and surrounding structures.
</div>

<div class="text" style="left:832px;top:280px;width:120px">Constructed of schedule 40, 3.5" steel tubing and powder coated for protection fro the elements.</div>
<div class="photo" style="left:956px;top:279px;width:201px;height:134px;background:linear-gradient(170deg,#d6d3cc 0%,#c2bfb7 35%,#2c5444 55%,#3a3b3c 85%)" role="img" aria-label="Standard Bin Sentinel installed around a dumpster on asphalt"></div>

<!-- Expandable -->
<div class="section-bracket" style="left:828px;top:446px;width:342px">
  <svg width="342" height="56">
    <path d="M11,56 V24 Q11,14 24,14 H300 Q334,14 334,50 V56" fill="none" stroke="#d0d0d0" stroke-width="16" transform="translate(4,4)"/>
    <path d="M11,56 V24 Q11,14 24,14 H300 Q334,14 334,50 V56" fill="none" stroke="var(--gold)" stroke-width="16"/>
  </svg>
  <div class="label">EXPANDABLE</div>
</div>

<div class="photo" style="left:913px;top:493px;width:185px;height:123px;background:linear-gradient(180deg,#a9c2de 0%,#b7b0a4 35%,#2d5444 55%,#4a4b4c 75%,#3c3d3e 100%)" role="img" aria-label="Expandable Bin Sentinel rail beside a dumpster in a parking lot"></div>
<div class="text" style="left:830px;top:629px;width:335px">
  <span class="brand">The Bin Sentinel™</span> Expandable is designed to provide maximum protection of masonry enclosures and surrounding structures. Constructed of schedule 40, 3.5" steel tubing and powder coated protects it from the elements.
</div>

<div class="photo" style="left:914px;top:722px;width:184px;height:120px;background:linear-gradient(180deg,#b8cde3 0%,#8a6d5a 40%,#3a3a38 55%,#9c9c9a 75%,#b0b0ad 100%)" role="img" aria-label="Expandable Bin Sentinel holding three containers behind a building"></div>
<div class="text" style="left:830px;top:856px;width:335px">
  <span class="brand">The Bin Sentinel™</span> Expandable can accomodate multiple containers up to 8 yards.
</div>

</body>
</html>
```